Crestline Gas and Plumbing Business Card Design

I am after a business card design for my plumbing business called 'Crestline Gas & Plumbing'. I do all types of plumbing and gas work and specialise in general maintenance plumbing. Would like to see designs using current logo

Industry/Entity Type

Plumbing

Contact Information for Business Card

Name - Dale Whitcombe
Phone number - 0455163027
Email - admin@crestlinegasandplumbing.example.com.au
ABN - 68204915336

```html
<!DOCTYPE html>
<html lang="en">
<head>
<meta charset="utf-8">
<title>Crestline Gas &amp; Plumbing – Business Card</title>
<link href="https://fonts.googleapis.com/css2?family=Open+Sans:wght@400;700&display=swap" rel="stylesheet">
<style>
  :root {
    --page-bg: #d6d6d6;
    --navy: #2e3192;
    --mid-blue: #0f75bd;
    --brand-blue: #1f4fa3;
    --orange: #f7931e;
    --ink: #333333;
    --muted: #5a5a5a;
    --white: #ffffff;
  }
  * { box-sizing: border-box; margin: 0; padding: 0; }
  html, body {
    width: 1200px; height: 900px; overflow: hidden;
    background: var(--page-bg);
    font-family: "Open Sans", Arial, sans-serif;
  }
  .canvas { position: relative; width: 1200px; height: 900px; }

  .card {
    position: absolute;
    width: 520px; height: 316px;
    border-radius: 18px;
    overflow: hidden;
  }

  /* Front */
  .card--front {
    left: 50px; top: 130px;
    background:
      linear-gradient(135deg, var(--navy) 0%, var(--navy) 22%, var(--mid-blue) 50%, var(--navy) 78%, var(--navy) 100%);
    display: flex; align-items: center; justify-content: center;
  }
  .brand { display: flex; align-items: center; gap: 14px; }
  .brand__dot { width: 18px; height: 18px; border-radius: 50%; background: var(--orange); flex: none; }
  .brand__name {
    font-weight: 700; color: var(--white);
    font-size: 30px; line-height: 1.1; letter-spacing: 0.5px;
  }

  /* Back */
  .card--back { left: 630px; top: 450px; background: var(--white); }
  .back__wave { position: absolute; left: 0; top: 0; width: 520px; height: 316px; }
  .back__brand { position: absolute; right: 28px; top: 26px; gap: 10px; }
  .back__brand .brand__name { color: var(--brand-blue); font-size: 22px; text-align: right; }
  .back__brand .brand__dot { width: 12px; height: 12px; }

  .person { position: absolute; right: 30px; top: 100px; text-align: right; }
  .person__name { color: var(--brand-blue); font-size: 17px; font-weight: 400; }
  .person__role { color: var(--muted); font-size: 12px; }

  .contact { position: absolute; right: 30px; top: 160px; text-align: right; font-size: 11.5px; color: var(--ink); line-height: 1.65; }
  .contact__abn-label { color: var(--orange); }
  .contact__row { display: flex; justify-content: flex-end; align-items: center; gap: 6px; }
  .contact__icon { width: 11px; height: 11px; flex: none; }
</style>
</head>
<body>
<main class="canvas">

  <section class="card card--front" aria-label="Card front">
    <div class="brand">
      <span class="brand__dot"></span>
      <span class="brand__name">Crestline<br>Gas &amp; Plumbing</span>
    </div>
  </section>

  <section class="card card--back" aria-label="Card back">
    <svg class="back__wave" viewBox="0 0 520 316" aria-hidden="true">
      <defs>
        <linearGradient id="waveFill" x1="0" y1="0" x2="1" y2="1">
          <stop offset="0" stop-color="#2e3192"/>
          <stop offset="0.5" stop-color="#0f75bd"/>
          <stop offset="1" stop-color="#2e3192"/>
        </linearGradient>
      </defs>
      <path d="M0 120 C70 100 130 110 170 160 C200 200 215 260 240 316 L0 316 Z" fill="url(#waveFill)"/>
    </svg>

    <div class="brand back__brand">
      <span class="brand__dot"></span>
      <span class="brand__name">Crestline<br>Gas &amp; Plumbing</span>
    </div>

    <div class="person">
      <p class="person__name">Dale Whitcombe</p>
      <p class="person__role">Founder</p>
    </div>

    <div class="contact">
      <p><span class="contact__abn-label">ABN:</span> 68204915336</p>
      <p class="contact__row">0455163027
        <svg class="contact__icon" viewBox="0 0 12 12" aria-hidden="true"><path d="M3 1 L5 3.5 L4 5 C5 7 6 8 7.5 8.5 L9 7.5 L11 9.5 L9.5 11 C5 10.5 1.5 7 1 2.5 Z" fill="#f7931e"/></svg>
      </p>
      <p class="contact__row">admin@crestlinegasandplumbing.example.com.au
        <svg class="contact__icon" viewBox="0 0 12 12" aria-hidden="true"><rect x="1" y="2.5" width="10" height="7" fill="none" stroke="#f7931e" stroke-width="1.4"/><path d="M1 2.5 L6 6.5 L11 2.5" fill="none" stroke="#f7931e" stroke-width="1.4"/></svg>
      </p>
      <p class="contact__row">www.crestlinegasandplumbing.example.com.au
        <svg class="contact__icon" viewBox="0 0 12 12" aria-hidden="true"><circle cx="6" cy="6" r="5" fill="none" stroke="#f7931e" stroke-width="1.3"/><path d="M1 6 H11 M6 1 C3.5 4 3.5 8 6 11 M6 1 C8.5 4 8.5 8 6 11" fill="none" stroke="#f7931e" stroke-width="1"/></svg>
      </p>
    </div>
  </section>

</main>
</body>
</html>
```